Accounting firm needing business card / letterhead designed
Marcus T. Elbering, CPA
marcus@fernquill.com
www.fernquill.com
482 N Harlow Ave Larchmere, OH 43719
419-555-0172

```html
<!DOCTYPE html>
<html lang="en">
<head>
<meta charset="utf-8">
<title>Fernquill Solutions – Business Card</title>
<link href="https://fonts.googleapis.com/css2?family=Open+Sans:wght@400;600;700&display=swap" rel="stylesheet">
<style>
  :root {
    --navy: #27226a;
    --lime: #8dc63f;
    --paper: #ffffff;
    --ink: #1f1f2e;
    --rule: #3a3a4a;
    --stage: #2b2b2e;
  }
  * { box-sizing: border-box; margin: 0; padding: 0; }
  html, body {
    width: 1200px; height: 904px; overflow: hidden;
    background: var(--stage);
    font-family: "Open Sans", Arial, sans-serif;
  }
  .sheet {
    position: relative; width: 1200px; height: 904px;
    display: flex; flex-direction: column; align-items: center; justify-content: center; gap: 56px;
  }
  .card {
    position: relative; width: 640px; height: 366px;
    box-shadow: 0 10px 26px rgba(0,0,0,.45);
  }
  .card--front { background: var(--navy); display: flex; align-items: center; justify-content: center; }
  .card--back { background: var(--paper); }

  .wordmark {
    display: flex; align-items: center; gap: 12px;
    font-weight: 700; font-size: 34px; letter-spacing: 2px; text-transform: uppercase;
    white-space: nowrap;
  }
  .wordmark__dot { width: 14px; height: 14px; border-radius: 50%; }
  .card--front .wordmark { color: #ffffff; }
  .card--front .wordmark__dot { background: var(--lime); }
  .card--back .wordmark { position: absolute; top: 80px; left: 0; right: 0; justify-content: center; color: var(--navy); }
  .card--back .wordmark__dot { background: var(--lime); }

  .holder {
    position: absolute; left: 56px; bottom: 74px;
    font-weight: 700; font-size: 23px; color: var(--navy); white-space: nowrap;
  }
  .divider {
    position: absolute; left: 352px; top: 190px; width: 1.5px; height: 110px; background: var(--rule);
  }
  .contact {
    position: absolute; left: 374px; top: 188px;
    font-size: 14.5px; line-height: 22px; color: var(--ink);
    list-style: none; white-space: nowrap;
  }
  .contact__address { margin-bottom: 4px; }
  .contact__row { display: flex; align-items: center; gap: 9px; }
  .contact__icon { width: 13px; height: 13px; flex: none; }
</style>
</head>
<body>
<main class="sheet">
  <section class="card card--front" aria-label="Card front">
    <div class="wordmark"><span class="wordmark__dot"></span>Fernquill Solutions</div>
  </section>

  <section class="card card--back" aria-label="Card back">
    <div class="wordmark"><span class="wordmark__dot"></span>Fernquill Solutions</div>

    <p class="holder">Marcus T. Elbering, CPA</p>
    <div class="divider"></div>

    <ul class="contact">
      <li class="contact__address">482 N Harlow Ave Larchmere<br>OH 43719</li>
      <li class="contact__row">
        <svg class="contact__icon" viewBox="0 0 16 16" aria-hidden="true"><circle cx="8" cy="8" r="8" fill="var(--navy)"/><path d="M5 4.2l1.6-.4.9 2-1 .8a5 5 0 0 0 2.9 2.9l.8-1 2 .9-.4 1.6c-3.6.4-7.2-3.2-6.8-6.8z" fill="#fff"/></svg>
        555-555-0172
      </li>
      <li class="contact__row">
        <svg class="contact__icon" viewBox="0 0 16 16" aria-hidden="true"><circle cx="8" cy="8" r="8" fill="var(--navy)"/><rect x="4" y="5.2" width="8" height="5.6" fill="#fff"/><path d="M4 5.4l4 3 4-3" stroke="var(--navy)" stroke-width="1" fill="none"/></svg>
        marcus@fernquill.com
      </li>
      <li class="contact__row">
        <svg class="contact__icon" viewBox="0 0 16 16" aria-hidden="true"><circle cx="8" cy="8" r="8" fill="var(--navy)"/><g stroke="#fff" stroke-width="1" fill="none"><circle cx="8" cy="8" r="4.5"/><ellipse cx="8" cy="8" rx="2" ry="4.5"/><path d="M3.5 8h9"/></g></svg>
        www.fernquill.com
      </li>
    </ul>
  </section>
</main>
</body>
</html>
```